Newly created Management Consulting company needs a brochure to capture clients's interest

This is a new management consulting firm providing service in Finance, Marketing, Operations/Manufacturing Strategy, and Project Management.
Please go to the company's website: www.veltanorpartners.ca . The website is pretty straightforward and gives a clear explanation of all the services and sub-services offered. Based on the existent material on the website, I would like to create a company's brochure that can inspire clients to seek our services.
One important thing: the slogan/tagline ("Shaping the future of your business") needs to be added somewhere in the vicinity of our company's' LOGO. Please see attached the company's logo (JPEG file).
The brochure size and number of pages can vary, depending on the layout of the brochure so it can fit the content, so I am open to different and innovative sizes/shapes and no. of pages etc. Graphics should combine real pictures with graphic design technology, and should give a professional look and feel comparable to big companies' marketing materials.
Updates
The brochure does not necessarily have to include pictures that are on the website. If you think that other pictures and graphics can deliver a stronger message to customers, by all means I am open to any other ideas.
Thanks.
As I said before, the pictures do not need to be exactly the same pictures as on the website, if you can bring in other cool pictures to attract clients, please go ahead. Also, you do not need to use only black background, if you have better colors ideas to combine with the our LOGO, and it looks good, by all means do use other colors. But our LOGO needs to be represented as it is on the JPEG I attached.
May the most creative and cool design win! Good luck!
Please ensure that all the content of our website fits into your brochure, including our contact information. It is up to you to come up with the necessary number of pages, design and shape of the brochure, but the text should be clear enough to be read by a normal person without a magnifying glass.
Thank you.
In order to keep the brochure to a reasonable number of pages, I agree that it is not necessary to include 100% all the text that appears on the website. That being said, even if you do not have enough space to include all the background and introduction paragraphs under each service/sub-service, it is still important that the main message for each service/sub-service is being contained in the brochure.
Target Market(s)
Our clients are companies with sizes starting from 10-20 employees and up to large Larkspan 700 companies.
Industry/Entity Type
Management Consulting
Look and feel

```html
<!DOCTYPE html>
<html lang="en">
<head>
<meta charset="utf-8">
<title>Veltanor Partners – Brochure Spreads</title>
<link href="https://fonts.googleapis.com/css2?family=Crimson+Pro:ital,wght@0,400;0,600;1,400;1,600&display=swap" rel="stylesheet">
<style>
:root{
  --green:#6aaa3a;
  --ink:#1c1c1c;
  --black:#0b0b0b;
  --paper:#ffffff;
  --mist:#e4e4e4;
  --line:#9a9a9a;
}
*{margin:0;padding:0;box-sizing:border-box}
html,body{width:1200px;height:849px;overflow:hidden;background:#fff}
body{position:relative;font-family:"Crimson Pro",Georgia,serif;color:var(--ink)}
.spread{position:absolute;width:551px;height:368px;border:1px solid var(--line);display:flex}
.spread--cover{left:33px;top:44px}
.spread--about{left:612px;top:44px;width:550px}
.spread--services{left:33px;top:448px}
.panel{position:relative;height:100%;overflow:hidden}
.panel--left{width:276px;border-right:1px solid var(--line)}
.panel--right{flex:1}
.mist{background:radial-gradient(ellipse at 45% 40%,#fdfdfd 0%,#f0f0f0 55%,var(--mist) 100%)}
.photo{position:absolute}
.body-text{font-size:4.3px;line-height:5.6px;text-align:justify}
.body-text p+p{margin-top:5px}
.green{color:var(--green)}
.sq{position:absolute;background:var(--green)}

/* cover spread */
.contact{position:absolute;left:14px;top:320px;font-size:4.6px;line-height:5.8px;font-style:italic}
.contact p+p{margin-top:5px}
.office{position:absolute;right:13px;top:324px;font-size:4.6px;line-height:5.8px;text-align:right}
.office strong{font-style:italic;font-weight:400}
.cover-photo{left:0;top:0;width:100%;height:308px;background:linear-gradient(160deg,#e9edf0 0%,#c6ced3 40%,#7f8a92 70%,#4b545b 100%)}
.logo-box{position:absolute;left:13px;top:0;width:78px;height:64px;background:var(--black);display:flex;align-items:center;justify-content:center;gap:5px;flex-direction:column}
.logo-box .mark{width:8px;height:8px;background:var(--green);border-radius:50%}
.logo-box .name{color:#fff;font-size:9px;letter-spacing:.6px}
.tagline{position:absolute;left:0;top:295px;width:100%;height:11px;background:rgba(255,255,255,.55);font-size:5.2px;font-weight:600;text-align:center;line-height:11px}
.cover-band{position:absolute;left:0;top:308px;width:100%;height:60px;background:var(--black)}
.pill{position:absolute;top:313px;width:48px;height:48px;border-radius:50%;background:#f3f3f3;color:var(--green);font-size:5.2px;font-weight:600;display:flex;align-items:center;justify-content:center;text-align:center;line-height:6px}

/* about spread */
.promise{position:absolute;left:84px;top:170px;width:104px;font-size:4.6px;line-height:5.6px;font-style:italic;color:var(--green)}
.intro{position:absolute;left:22px;top:24px;width:196px;font-size:4.4px;line-height:5.6px;font-style:italic;font-weight:600;text-align:justify}
.tab{position:absolute;right:0;top:25px;width:20px;height:52px;background:var(--green)}
.pillar{position:absolute;top:104px;width:71px}
.pillar .photo{position:relative;width:71px;height:42px}
.pillar h3{font-size:5.4px;font-weight:400;color:var(--green);margin:13px 0 7px;letter-spacing:.2px}
.pillar .body-text{text-align:left;font-size:3.9px;line-height:5.1px}

/* services spread */
.services-title{position:absolute;left:140px;top:58px;font-size:12px;line-height:12px;color:var(--green);font-weight:400}
.services-sub{position:absolute;left:140px;top:72px;font-size:8px;letter-spacing:.3px;font-weight:400}
.lead{position:absolute;left:23px;top:94px;width:230px;font-size:4.3px;line-height:5.5px;font-style:italic;font-weight:600;text-align:justify}
.section-title{position:absolute;font-size:8.2px;font-weight:400}
.float-photo{float:right;width:78px;height:52px;margin:0 0 4px 6px}
.wrap-space{float:right;width:96px;height:26px}
.lower{position:absolute;left:0;top:204px;width:100%;height:164px}
</style>
</head>
<body>

<!-- Spread 1: back cover and front cover -->
<section class="spread spread--cover">
  <div class="panel panel--left mist">
    <div class="contact">
      <p>To get in touch with one of our consultants,<br>please use one of the following options:</p>
      <p>Phone: 778-555-0142 &nbsp;|&nbsp; Fax: 778-555-0187<br>Email: info@veltanorpartners.ca</p>
    </div>
    <div class="office">
      <strong>Office Address</strong><br>
      Suite 410, Harbourline Tower,<br>
      270 Cedarmere Street, Vancouver<br>
      BC V6B 0P4, Canada
    </div>
  </div>
  <div class="panel panel--right">
    <div class="photo cover-photo" role="img" aria-label="Business people shaking hands in a bright glass office lobby"></div>
    <div class="logo-box">
      <span class="mark"></span>
      <span class="name">VELTANOR</span>
    </div>
    <div class="tagline">Shaping the future of your business</div>
    <div class="cover-band"></div>
    <div class="pill" style="left:20px">FINANCE</div>
    <div class="pill" style="left:80px">MARKETING</div>
    <div class="pill" style="left:140px">OPERATIONS</div>
    <div class="pill" style="left:200px">PROJECT<br>MANAGEMENT</div>
  </div>
</section>

<!-- Spread 2: about the firm -->
<section class="spread spread--about">
  <div class="panel panel--left mist">
    <p class="promise">We are committed to help our clients build enduring businesses, sustain competitive advantage and grow stronger in even uncertain market conditions.</p>
  </div>
  <div class="panel panel--right" style="background:var(--paper)">
    <p class="intro">Veltanor Partners chief focus is addressing the critical business challenges of our clients. We work across all industries and guide our customers in making the right decisions and conducting the best course of action in operations, marketing, and finance. We come up with solutions for a company that will improve performance, reduce costs and maximize growth. Our dedicated, professional team consists of MBAs and engineers of high standing with a variety of educational and industry experiences. They bring their intelligence and analytical skills to every client. Above all, they are passionate about taking on new challenges and share a deep commitment to excellence.</p>
    <div class="tab"></div>

    <div class="pillar" style="left:22px">
      <div class="photo" role="img" aria-label="Young plant sprouting from soil in cupped hands" style="background:linear-gradient(180deg,#f2f2f2,#9a9a9a)"></div>
      <h3>OUR VALUES</h3>
      <div class="body-text">
        <p>Our values are the essence of our company's identity. Our core values are driven by our mission to help our clients overcome their business challenges and become successful in their markets. We firmly believe that we will be successful if our clients are successful.</p>
        <p>At Veltanor Partners, we strive to create a working environment where every employee can achieve his or her full potential.</p>
        <p>We build productive, long-lasting relationships with our clients.</p>
      </div>
    </div>

    <div class="pillar" style="left:102px">
      <div class="photo" role="img" aria-label="Close-up of a handshake against a blue sky" style="background:linear-gradient(160deg,#3b6fb8,#8a4a3a 60%,#2a4f8c)"></div>
      <h3>OUR MISSION</h3>
      <div class="body-text">
        <p>Our mission is to help our clients overcome their challenges, gain distinctive advantage in their industries and become successful in their markets. We will undertake only value-added consulting assignments that result in direct contribution to our clients' profitability. We believe in delivering real value to our clients and being accountable for our results.</p>
      </div>
    </div>

    <div class="pillar" style="left:182px">
      <div class="photo" role="img" aria-label="Two business people in suits shaking hands" style="background:linear-gradient(160deg,#f4f6f8,#9aa6b2 60%,#3d4a5a)"></div>
      <h3>OUR APPROACH</h3>
      <div class="body-text">
        <p>At Veltanor Partners nothing is more important to us than the relationship we build with our clients. It is our pledge to all our clients that our work will always be conducted at the highest level of integrity, honesty, and confidentiality. Whether we are working with a Larkspan 700 company or a small business start-up, it is our commitment to do the best we can for a company.</p>
        <p>We strive to offer our clients' peace of mind. We are so confident in the value that we provide that we offer a 100% Money Back Guarantee, in the event that we do not meet a client's expectations.</p>
      </div>
    </div>
  </div>
</section>

<!-- Spread 3: finance services -->
<section class="spread spread--services">
  <div class="panel panel--left mist">
    <div class="photo" role="img" aria-label="Businessman standing before a large blue stock market display" style="left:22px;top:0;width:107px;height:84px;background:linear-gradient(180deg,#2a5fb0,#12306a 70%,#0a1c44)"></div>
    <h1 class="services-title">OUR SERVICES</h1>
    <h2 class="services-sub">FINANCE</h2>
    <p class="lead">Making optimal corporate financial decisions to support the execution of corporate strategies has become increasingly challenging in today's competitive and volatile markets. Good, optimal decisions are made based on a thorough understanding of financial information, value creation as well as all aspects of a particular business. Veltanor Partners can support and advise clients in a variety of industries with their strategic and corporate finance issues in order to maximize shareholder value. Our consultants take a holistic view at the corporate finance and use data-driven cases to help companies understand their sources of valuation advantage and increase returns to shareholders.</p>

    <div class="sq" style="left:0;top:175px;width:10px;height:13px"></div>
    <h3 class="section-title" style="left:23px;top:176px">Capital Budgeting Services</h3>
    <div class="body-text" style="position:absolute;left:23px;top:192px;width:230px">
      <div class="float-photo" role="img" aria-label="Calculator, coins and financial charts on a desk" style="background:linear-gradient(150deg,#dfe8f2,#7b96b8 60%,#37506e)"></div>
      <p>Capital budgeting is the process of analysing different investment opportunities and deciding which ones to implement. For example, a company has to determine whether to build a new plant or to sink money in an existing facility. Which long-term venture is worth pursuing and will have the greater payoff? Managers need to measure each opportunity's potential in order to compare the projected result, and then make their decision on that information.</p>
      <p>As you can see, a capital budgeting decision defines the future direction and growth of the company. When a company decides on an investment project, the results of that investment decision will affect the business for many years, so care must be taken. Poor capital budgeting can have serious financial consequences. Another example is if a company invests too much in new equipment, it will incur unnecessary high depreciation and other expenses. On the flip-side, if a company does not invest enough, its equipment may not be modern enough to enable it to produce competitively.</p>
      <p>These choices carry profound consequences for a company. When you look closely at running a business, you can see that it is nothing more than a constant exercise in capital budgeting decisions.</p>
      <p>Our consultants help our clients determine capital budgeting decisions by focusing on net present value (NPV) analysis. This determines the effect of each capital budgeting proposal on the company's cash flow, and the consequences of the decision on the company's value. In addition, our consultants will conduct a sensitivity analysis. This helps the client understand which aspects of a project under consideration are the most critical.</p>
    </div>
  </div>

  <div class="panel panel--right" style="background:var(--paper)">
    <div class="photo" role="img" aria-label="Blue globe resting on printed financial tables" style="left:0;top:20px;width:91px;height:58px;background:linear-gradient(150deg,#e9eff6,#6d8fbf 55%,#1f3f78)"></div>
    <h3 class="section-title" style="left:15px;top:89px">Business Valuation Services</h3>
    <div class="body-text" style="position:absolute;left:15px;top:102px;width:114px">
      <p>Knowing what their company is worth is a key element in any number of major decisions management may have to consider. Valuing a business requires a deep understanding and analysis of an industry and the firm's position in it. A firm's strategy, products or services, consumer demand, and competitiveness in the industry are just some of the elements determining a company's worth. These are only a few of the characteristics explored when Veltanor Partners values your business. Valuing all or part of a business requires forecasting the future of the business, which in turn requires a disciplined analysis of speculative information and of the financial statements. Good thinking, good application and a good balance between costs and benefits constitute the main ingredients of business valuation.</p>
    </div>
    <div class="body-text" style="position:absolute;left:145px;top:20px;width:113px">
      <p>Our consultants use their knowledge and expertise to build the best valuation product for our clients and help them understand any gaps between market value and intrinsic value. We provide recommendations that create value for our clients in the event of:</p>
      <p>- Merger and Acquisition – we help clients understand the value and synergy to be created through the transaction.</p>
      <p>- Divestitures – we show clients how inefficiencies and negative synergies are eliminated, how the strategic fit and focus are enhanced, and how these affect the market value of their firm.</p>
      <p>We perform three common valuation methods, using our proprietary models:</p>
      <p style="text-align:left">- Enterprise Discounted Cash Flow<br>- Discounted Economic Profit<br>- Multiples Analysis</p>
      <p>Each method has its advantages and disadvantages; however we pay close attention to the valuation ranges and all the other factors described above before we make any recommendations to our clients.</p>
    </div>
    <div class="sq" style="right:0;top:98px;width:10px;height:12px"></div>

    <div class="lower mist">
      <div class="sq" style="left:0;top:4px;width:10px;height:12px"></div>
      <h3 class="section-title" style="left:16px;top:5px">Value-Based Management</h3>
      <div class="photo" role="img" aria-label="Pen resting on a printed bar chart of revenue growth" style="right:0;top:0;width:90px;height:50px;background:linear-gradient(160deg,#f1f4f8,#9fb5d4 50%,#3a67a8)"></div>
      <div class="body-text" style="position:absolute;left:16px;top:26px;width:242px">
        <span class="wrap-space" aria-hidden="true"></span>
        <p>Increasing the company value is the primary goal for managers. However, meeting quarterly goals is not the same as creating sustainable, long-term value for the shareholders. Managers should balance short-term financial performance against maintaining sustained strong growth and creating value for decades ahead. In fact, pursuing the creation of long-term, sustainable shareholder value is good for all the stakeholders. It creates more jobs, allows companies to show greater commitment in meeting their social responsibilities, and builds the company's reputation and relationships in new markets. This enables the company to be a trusted investment, employer, trade partner, and tax payer.</p>
        <p>Focusing on long-term value creation is a tough job but by relying on data, thoughtful analysis, and a deep understanding of the competitive dynamics in the industry, it can be accomplished. Managers should make decisions on the key driver of value and align their company's overall aspirations, analytical techniques, and management processes to focus on it.</p>
        <p>Veltanor Partners partners with clients to help develop and implement Value Based Management (VBM) strategy and philosophy. This concentrates their businesses on striving to achieve what's important. We help clients fully understand the economic value of their company, identify areas for performance improvement, and implement the most effective strategies for increasing shareholder value.</p>
      </div>
    </div>
  </div>
</section>

</body>
</html>
```